Real Estate 24"x24" Sign, Business Card, Letter Head and Envelope

This is a 4 project contest. If we choose a design or designs we like from what you sent we are willing to pay an amount at our discretion for that design even if we don't like all your designs for the 4 projects. Please be creative. Attached are our logo files. Please message us with any questions. Thanks and Good Luck!
Project 1: QMTD Realty 24" x 24" yard sign
We want to use the same blue background in our logo for the sign where the logo in white font will be on. CMYK 100,80,0,0. Attached is a sample a local designer made for you to get an idea what we are looking for. In the sample, the website is way too big and the entire sign is very plain and not attractive looking plus blue color is wrong one. We want the logo on top as large as possible but keeping it proportionate and attractive looking buy not too big that it looks odd. The following information can go in white color background or same blue color background color. Our company colors are blue (as per logo), green (as per logo), and white. "Residential & Commercial" goes under the logo. Under that put our phone number "312-640-5918" as large as possible but still looks good and under that our website in much smaller but readable font "www.qmtdrealty.com".
Project 2: Envelope
We have two version of the logo. Use one or both. Whatever looks best in your design. The envelope will be white. We only want on top left corner logo and underneath our mailing address: 5147 Hawthorne Ave. Skokie, IL 60091-2714. Maybe some creative decorative design at bottom of envelope will look nice
Project 3: Letter Head
We have two version of the logo. Use one or both. Whatever looks best in your design. We want the following information on the top of the letterhead. Logo, address: 5147 Hawthorne Ave., Skokie, IL 60091-2714, phone: 312-640-5918, fax: 312-918-6057 website www.qmtdrealty.com, email: info@qmtdrealty.com
Project 4: Business card
Use either logo. We need cards for two individuals. Information for Person 1: Dev Mehta, Managing Broker, Phone: 312-640-5918, Email: dev.mehta@qmtdrealty.com. Person 2: Raj Mehta Broker Phone: 312-285-3390 Email: raj.mehta@qmtdrealty.com. Add Address, Fax and website same as above letter head.

```html
<!DOCTYPE html>
<html lang="en">
<head>
<meta charset="utf-8">
<title>QMTD Realty Yard Sign</title>
<link rel="stylesheet" href="https://fonts.googleapis.com/css2?family=Montserrat:wght@600;700;800&display=swap">
<style>
  :root {
    --brand-blue: #2457b2;
    --brand-blue-deep: #1d479a;
    --brand-green: #6cc04a;
    --white: #ffffff;
    --backdrop: #e9ebee;
  }
  * { margin: 0; padding: 0; box-sizing: border-box; }
  html, body {
    width: 1200px;
    height: 822px;
    overflow: hidden;
    background: var(--backdrop);
  }
  .canvas {
    position: relative;
    width: 1200px;
    height: 822px;
  }
  .yard-sign {
    position: absolute;
    left: 240px;
    top: 41px;
    width: 740px;
    height: 740px;
    background: var(--brand-blue);
    overflow: hidden;
    font-family: "Montserrat", Arial, sans-serif;
    color: var(--white);
  }
  .sign-photo {
    position: absolute;
    left: 150px;
    top: 170px;
    width: 590px;
    height: 430px;
    background: linear-gradient(180deg,
      rgba(36, 87, 178, 0) 0%,
      rgba(80, 125, 200, 0.35) 35%,
      rgba(60, 105, 185, 0.45) 70%,
      rgba(36, 87, 178, 0) 100%);
  }
  .accent-frame {
    position: absolute;
    left: 0;
    top: 0;
    width: 740px;
    height: 740px;
  }
  .brand-mark {
    position: absolute;
    left: 42px;
    top: 96px;
    display: flex;
    align-items: center;
    gap: 18px;
  }
  .brand-square {
    width: 34px;
    height: 34px;
    background: var(--white);
  }
  .brand-name {
    font-weight: 800;
    font-size: 74px;
    line-height: 0.95;
    letter-spacing: -1px;
    color: var(--white);
  }
  .services {
    position: absolute;
    left: 40px;
    top: 470px;
    font-weight: 700;
    font-size: 39px;
    line-height: 1.1;
    letter-spacing: 0.5px;
  }
  .phone-box {
    position: absolute;
    left: 36px;
    top: 560px;
    width: 600px;
    height: 92px;
    background: var(--white);
    display: flex;
    align-items: center;
    justify-content: center;
  }
  .phone-number {
    font-weight: 700;
    font-size: 74px;
    letter-spacing: -0.5px;
    color: var(--brand-green);
  }
  .website {
    position: absolute;
    left: 40px;
    top: 670px;
    font-weight: 700;
    font-size: 38px;
    letter-spacing: 0.5px;
  }
</style>
</head>
<body>
<main class="canvas">
  <section class="yard-sign" aria-label="QMTD Realty yard sign">
    <div class="sign-photo" role="img" aria-label="Blue-tinted photo of a two-storey suburban house"></div>

    <svg class="accent-frame" viewBox="0 0 740 740" aria-hidden="true">
      <polyline points="395,205 700,205 700,712" fill="none" stroke="var(--brand-green)" stroke-width="5"/>
    </svg>

    <div class="brand-mark">
      <span class="brand-square"></span>
      <span class="brand-name">QMTD<br>Realty</span>
    </div>

    <p class="services">Residential<br>Commercial</p>

    <div class="phone-box">
      <span class="phone-number">312-640-5918</span>
    </div>

    <p class="website">qmtdrealty.com</p>
  </section>
</main>
</body>
</html>
```